Best website on the WWW

I am looking to create a multi tab wesbite to revamp our outdated website.

Here is an example of a companies website I really like
https://ridgelinehaulers.example/

Target Market(s)

New customers, government agency's

Industry/Entity Type

Auto repair, towing and recovery, hazmat clean up

Coding

Coded - Design and coding required

Number of Pages Required

5+ page

Font styles to use
Sans Serif

Requirements
Nice to have
• I would like to see an interactive website, that includes details and photos from our companies

```html
<!DOCTYPE html>
<html lang="en">
<head>
<meta charset="utf-8">
<title>Ridgeline Haulers — Repair &amp; Towing</title>
<link href="https://fonts.googleapis.com/css2?family=Oswald:wght@500;600&family=Poppins:wght@400;500;600&display=swap" rel="stylesheet">
<style>
:root{
  --accent:#f4a41c;
  --dark:#221e1b;
  --ink:#1c1c1c;
  --muted:#6b6b6b;
  --light:#efefef;
  --footer:#1a1a1a;
  --white:#fff;
  --line:#d8d8d8;
}
*{margin:0;padding:0;box-sizing:border-box}
html,body{width:1200px;height:3473px;overflow:hidden}
body{position:relative;font-family:'Poppins',sans-serif;color:var(--ink);background:var(--white)}
.abs{position:absolute}
.head{font-family:'Oswald',sans-serif;font-weight:500;text-transform:uppercase;letter-spacing:-.2px;line-height:1.15}
.body-text{font-size:9.5px;line-height:15px;color:var(--muted)}
section{position:absolute;left:0;width:1200px;overflow:hidden}
.tag{position:absolute;height:15px;background:var(--ink);color:#fff;font-size:8px;line-height:15px;padding-left:40px;padding-right:12px;text-transform:uppercase}
.tag::before{content:"";position:absolute;left:8px;top:2px;width:22px;height:11px;background:repeating-linear-gradient(90deg,#fff 0 3px,#999 3px 6px)}
.btn{position:absolute;background:var(--accent);color:#fff;font-family:'Oswald',sans-serif;font-size:9px;text-transform:uppercase;text-align:center}
.photo{position:absolute}

/* hero */
.hero{top:0;height:448px;background:#111}
.hero-photo{left:560px;top:0;width:640px;height:448px;background:radial-gradient(ellipse at 60% 35%,#b8894e 0,#7a5630 30%,#2a2018 65%,#111 100%)}
.hero-fade{left:0;top:0;width:760px;height:448px;background:linear-gradient(90deg,#111 65%,rgba(17,17,17,0))}
.topbar{top:0;left:0;width:1200px;height:22px;background:rgba(0,0,0,.5);font-size:8px;color:#ddd}
.nav a{position:absolute;top:35px;font-size:9px;color:#fff;text-decoration:none}
.logo{font-family:'Poppins',sans-serif;font-weight:600;color:#fff;font-size:15px;display:flex;align-items:center;gap:8px}
.logo i{display:block;width:14px;height:14px;border-radius:50%;background:var(--accent)}
.play{border-radius:50%;background:#fff;display:flex;align-items:center;justify-content:center}

/* services */
.svc-box{position:absolute;width:53px;height:53px;border:1px solid var(--line);display:flex;align-items:center;justify-content:center}
.svc-box.on{background:var(--accent);border-color:var(--accent)}
.svc-name{position:absolute;font-family:'Oswald',sans-serif;font-size:12px;line-height:21px;text-transform:uppercase}

/* dark */
.dark{background:var(--dark);color:#fff}
.faq{position:absolute;left:630px;width:297px;font-size:9px;font-weight:600}
.faq span{position:absolute;right:0;top:-3px;font-weight:400;font-size:13px;color:#aaa}
.rule{position:absolute;left:630px;width:297px;height:1px;background:#3a3532}

/* cards */
.card{position:absolute;top:2524px;width:325px;height:186px;border:1px solid #cfcfcf;background:#fff}
.check{display:inline-block;width:9px;height:6px;border-left:1.5px solid var(--accent);border-bottom:1.5px solid var(--accent);transform:rotate(-45deg);margin-right:8px;position:relative;top:-2px}

.news-title{position:absolute;font-family:'Oswald',sans-serif;font-weight:500;font-size:12px;line-height:21px;text-transform:uppercase}
.badge{position:absolute;left:6px;top:6px;background:var(--accent);color:#fff;font-size:6px;padding:1px 5px}

.foot-col{position:absolute;top:88px;font-size:8px;line-height:17px;color:#bbb}
.foot-col b{display:block;color:var(--accent);font-weight:500;margin-bottom:4px}
.dots{display:flex;gap:7px;height:17px;align-items:center}
.dots span{width:8px;height:8px;border-radius:50%;background:var(--accent)}
</style>
</head>
<body>

<!-- HERO -->
<section class="hero">
  <div class="photo hero-photo" role="img" aria-label="Close-up of a gold sports car front headlight and bumper"></div>
  <div class="abs hero-fade"></div>
  <div class="abs topbar">
    <span class="abs" style="left:264px;top:5px">Follow our socials</span>
    <span class="abs" style="left:354px;top:7px;width:8px;height:8px;border-radius:50%;background:#ddd"></span>
    <span class="abs" style="left:368px;top:7px;width:8px;height:8px;border-radius:50%;background:#ddd"></span>
    <span class="abs" style="left:382px;top:7px;width:8px;height:8px;border-radius:50%;background:#ddd"></span>
    <span class="abs" style="left:733px;top:5px">+123 456 789</span>
    <span class="abs" style="left:808px;top:5px;width:1px;height:11px;background:#777"></span>
    <span class="abs" style="left:821px;top:5px">Prds RD 99</span>
  </div>
  <div class="abs logo" style="left:250px;top:58px"><i></i>Ridgeline Haulers</div>
  <nav class="nav">
    <a style="left:582px;color:var(--accent)">Home</a>
    <a style="left:632px">Pages &nbsp;⌄</a>
    <a style="left:701px">Services</a>
    <a style="left:761px">Repair</a>
    <a style="left:811px">Performance</a>
    <a style="left:892px">Contact</a>
  </nav>
  <h1 class="abs head" style="left:264px;top:146px;font-size:44px;line-height:48px;color:#fff">Boost your car's<br>performance</h1>
  <p class="abs" style="left:264px;top:260px;width:290px;font-size:9px;line-height:14px;color:#ccc">Lorem ipsum dolor sit amet, consectetur adipiscing elit. Ut elit tellus, luctus nec ullamcorper mattis, pulvinar dapibus leo consectetur adipiscing elit.</p>
  <div class="btn" style="left:264px;top:326px;width:100px;height:34px;line-height:34px">Our Services</div>
  <div class="abs" style="left:388px;top:338px;font-size:9px;color:#ddd">◌&nbsp;&nbsp; Send Message</div>
  <div class="abs play" style="left:745px;top:229px;width:48px;height:48px">
    <svg width="14" height="14" viewBox="0 0 14 14"><path d="M3 1l10 6-10 6z" fill="#f4a41c"/></svg>
  </div>
</section>

<!-- SERVICES -->
<section style="top:448px;height:522px">
  <div class="tag" style="left:264px;top:64px">Services</div>
  <h2 class="abs head" style="left:264px;top:94px;font-size:27px">World class auto services</h2>
  <p class="abs body-text" style="left:264px;top:144px;width:350px">Lorem ipsum dolor sit amet, consectetur adipisicing elit, sed do eiusmod tempor incididunt ut labore et dolore magna aliqua. Ut enim ad minim veniam, laboris nisi ut aliquip ex ea commodo consequat.</p>

  <div class="svc-box" style="left:264px;top:209px"><svg width="24" height="24" fill="none" stroke="#f4a41c" stroke-width="1.4"><circle cx="12" cy="12" r="9"/><path d="M12 12l4-4M6 12h2M16 12h2M12 6v2"/></svg></div>
  <div class="svc-name" style="left:330px;top:214px">Complete<br>checking</div>
  <div class="svc-box" style="left:436px;top:209px"><svg width="24" height="24" fill="none" stroke="#f4a41c" stroke-width="1.4"><path d="M5 19l4-4M9 15l9-10 1 1-10 9z"/></svg></div>
  <div class="svc-name" style="left:502px;top:214px">Autobody<br>detailing</div>

  <div class="svc-box" style="left:264px;top:286px"><svg width="24" height="24" fill="none" stroke="#f4a41c" stroke-width="1.4"><path d="M6 18l3-1 8-8c2-2 2-5 2-5s-3 0-5 2l-8 8z"/><circle cx="14" cy="10" r="1.5"/></svg></div>
  <div class="svc-name" style="left:330px;top:291px">Express<br>autoservice</div>
  <div class="svc-box" style="left:436px;top:286px"><svg width="24" height="24" fill="none" stroke="#f4a41c" stroke-width="1.4"><path d="M5 5l14 14M19 5L5 19"/><circle cx="5" cy="5" r="2"/><circle cx="19" cy="19" r="2"/></svg></div>
  <div class="svc-name" style="left:502px;top:291px">Custom<br>modification</div>

  <div class="svc-box" style="left:264px;top:365px"><svg width="24" height="24" fill="none" stroke="#f4a41c" stroke-width="1.4"><circle cx="12" cy="8" r="3.5"/><path d="M5 21v-4c0-3 3-5 7-5s7 2 7 5v4z"/></svg></div>
  <div class="svc-name" style="left:330px;top:370px">Mobile help<br>towing</div>
  <div class="svc-box on" style="left:436px;top:365px"><svg width="24" height="24" fill="none" stroke="#fff" stroke-width="1.6"><circle cx="12" cy="12" r="9"/><circle cx="12" cy="12" r="3"/><path d="M12 12l5-3"/></svg></div>
  <div class="svc-name" style="left:502px;top:370px">Autospeed<br>booster</div>

  <div class="abs" style="left:264px;top:444px;font-size:8px;color:var(--muted)"><span style="color:var(--accent)">⊸</span>&nbsp;&nbsp; We are committed to contributing back to the community.</div>
  <div class="photo" style="left:668px;top:60px;width:269px;height:403px;background:linear-gradient(160deg,#8c9299,#4b4f55 45%,#2c2c2e 80%,#8a8c8f)" role="img" aria-label="Two mechanics working under the open hood of a car in a workshop"></div>
</section>

<!-- GUARANTEED -->
<section class="dark" style="top:970px;height:508px">
  <div class="photo" style="left:288px;top:60px;width:116px;height:121px;background:linear-gradient(135deg,#3a5a8a,#1e2a3c 60%,#9a7050)" role="img" aria-label="Hands working on an engine bay"></div>
  <div class="photo" style="left:404px;top:123px;width:145px;height:252px;background:linear-gradient(170deg,#c9d2dc,#6a6a6a 45%,#2b2622)" role="img" aria-label="Mechanics inspecting a car with the bonnet open"></div>
  <div class="photo" style="left:264px;top:316px;width:200px;height:134px;background:linear-gradient(90deg,#7a5c43,#3b2d24 55%,#2a3f5a)" role="img" aria-label="Close-up of a car wheel and side panel"></div>
  <h2 class="abs head" style="left:630px;top:98px;font-size:24px">Guaranteed auto services</h2>
  <p class="abs" style="left:630px;top:140px;width:300px;font-size:9px;line-height:15px;color:#bbb">Lorem ipsum dolor sit amet, consectetur adipisicing elit, sed do eiusmod tempor incididunt ut labore et dolore magna aliqua.</p>
  <div class="faq" style="top:203px;color:var(--accent)">How do I know when my car needs a tune up?<span>–</span></div>
  <div class="rule" style="top:224px"></div>
  <p class="abs" style="left:630px;top:236px;width:250px;font-size:9px;line-height:15px;color:#bbb">Lorem ipsum dolor sit amet, consectetur adipiscing elit. Ut elit tellus, luctus nec ullamcorper mattis, pulvinar incididunt ut labore et dolore magna.</p>
  <div class="faq" style="top:308px">How should I prepare my car for a road trip?<span>+</span></div>
  <div class="rule" style="top:328px"></div>
  <div class="faq" style="top:346px">What should I do if my car starts to overheat?<span>+</span></div>
  <div class="btn" style="left:630px;top:384px;width:100px;height:33px;line-height:33px">Appointment</div>
</section>

<!-- QUALITY -->
<section style="top:1478px;height:516px">
  <div class="tag" style="left:264px;top:66px">Expert</div>
  <h2 class="abs head" style="left:264px;top:96px;font-size:27px">Quality services</h2>
  <p class="abs body-text" style="left:264px;top:150px;width:180px">Lorem ipsum dolor sit amet, consectetur adipisicing elit, sed do eiusmod tempor incididunt ut labore et dolore magna aliqua.</p>
  <p class="abs body-text" style="left:264px;top:214px;width:180px">Ut enim ad minim veniam, laboris nisi ut aliquip ex ea commodo consequat dolore magna.</p>
  <div class="abs head" style="left:264px;top:278px;font-size:38px;color:var(--accent);font-style:italic;font-weight:600">47</div>
  <div class="abs head" style="left:357px;top:278px;font-size:38px;color:var(--accent);font-style:italic;font-weight:600">15</div>
  <div class="abs head" style="left:264px;top:326px;font-size:11px">Mechanics</div>
  <div class="abs head" style="left:349px;top:326px;font-size:11px">Workshops</div>
  <div class="photo" style="left:500px;top:60px;width:437px;height:294px;background:linear-gradient(180deg,#c7ccd1,#8d9398 40%,#55585c 75%,#6d6d6a)" role="img" aria-label="Flatbed tow truck being loaded beside a box trailer"></div>
  <div class="photo" style="left:937px;top:115px;width:202px;height:208px;background:linear-gradient(180deg,#8a9096,#6e7176 55%,#6b5a3c)" role="img" aria-label="Heavy recovery wrecker truck parked in a field"></div>
  <div class="abs" style="left:997px;top:349px;width:40px;height:4px;background:var(--ink)"></div>
  <div class="abs" style="left:1040px;top:350px;width:40px;height:2px;background:#999"></div>
  <div class="abs" style="left:1083px;top:350px;width:40px;height:2px;background:#999"></div>
</section>

<!-- SUPPORT -->
<section class="dark" style="top:1994px;height:344px"></section>
<div class="photo" style="left:268px;top:1887px;width:644px;height:220px;background:linear-gradient(180deg,rgba(60,60,60,.25) 0,#2b2b2b 40%,#1a1a1a 100%)" role="img" aria-label="Black sports coupe shown in side profile"></div>
<div class="abs play" style="left:575px;top:1976px;width:48px;height:48px">
  <svg width="14" height="14" viewBox="0 0 14 14"><path d="M3 1l10 6-10 6z" fill="#f4a41c"/></svg>
</div>
<div class="abs" style="left:264px;top:2108px;color:var(--accent);font-size:10px;letter-spacing:3px">★★★★★</div>
<p class="abs" style="left:264px;top:2138px;width:355px;font-size:13px;line-height:19px;color:#fff">Lorem ipsum dolor sit amet, consectetur adipisicing elit, sed do eiusmod tempor ut labore et dolore magna aliqua. Ut enim ad minim veniam, quis nostrud ullamco laboris.</p>
<div class="abs" style="left:264px;top:2234px;width:40px;height:40px;border-radius:50%;background:linear-gradient(135deg,#bbb,#777)" role="img" aria-label="Reviewer portrait"></div>
<div class="abs" style="left:316px;top:2244px;font-size:8px;color:#fff">DANA HOLT<br><span style="color:#999">Verified</span></div>
<div class="abs" style="left:590px;top:2228px;font-family:'Oswald',sans-serif;font-size:40px;color:#fff;line-height:1">”</div>
<h2 class="abs head" style="left:700px;top:2136px;font-size:24px;color:#fff">Top notch support</h2>
<p class="abs" style="left:700px;top:2180px;width:210px;font-size:9px;line-height:15px;color:#bbb">Lorem ipsum dolor sit amet, consectetur adipisicing elit, sed do eiusmod tempor incididunt ut labore et dolore magna aliqua.</p>
<div class="abs" style="left:700px;top:2248px;font-size:8.5px;line-height:18px;color:#ccc"><span class="check"></span>4.95 Rating<br><span class="check"></span>Fast respond</div>
<div class="abs" style="left:815px;top:2248px;font-size:8.5px;line-height:18px;color:#ccc"><span class="check"></span>Easy access<br><span class="check"></span>Reasonable price</div>

<!-- INNOVATION -->
<section style="top:2338px;height:433px">
  <div class="tag" style="left:545px;top:57px">Innovation</div>
  <h2 class="abs head" style="left:0;width:1200px;text-align:center;top:86px;font-size:25px">Latest automotive technology</h2>
  <p class="abs body-text" style="left:400px;width:400px;text-align:center;top:134px">Lorem ipsum dolor sit amet, consectetur adipisicing elit, sed do eiusmod tempor incididunt ut labore et dolore magna aliqua.</p>
</section>
<div class="card" style="left:264px">
  <div class="photo" style="left:12px;top:10px;width:105px;height:160px;background:linear-gradient(180deg,#777,#3d3d3d 60%,#555)" role="img" aria-label="Mechanic standing in a garage"></div>
  <h3 class="abs head" style="left:134px;top:16px;font-size:17px;line-height:27px">Engine repair and<br>diagnosis</h3>
  <p class="abs body-text" style="left:134px;top:76px;width:175px;font-size:9px;line-height:14.5px">Lorem ipsum dolor sit amet, consectetur adipiscing elit. Ut elit tellus, luctus nec ullamcorper mattis, pulvinar dapibus leo. Lorena ipsum sit amet consectetur adipiscing elit. Ut elit tellus luctus nec.</p>
</div>
<div class="card" style="left:612px">
  <div class="photo" style="left:12px;top:10px;width:105px;height:160px;background:linear-gradient(180deg,#9a9a9a,#4a4a4a 55%,#8a5a30)" role="img" aria-label="Mechanic working beneath a car"></div>
  <h3 class="abs head" style="left:134px;top:16px;font-size:17px;line-height:27px">Engine performance<br>maintenance</h3>
  <p class="abs body-text" style="left:134px;top:76px;width:175px;font-size:9px;line-height:14.5px">Lorem ipsum dolor sit amet, consectetur adipiscing elit. Ut elit tellus, luctus nec ullamcorper mattis, pulvinar dapibus leo. Lorena ipsum sit amet consectetur adipiscing elit. Ut elit tellus luctus nec.</p>
</div>

<!-- BLOG -->
<section style="top:2771px;height:445px;background:var(--light)">
  <div class="tag" style="left:550px;top:58px">Autoblog</div>
  <h2 class="abs head" style="left:0;width:1200px;text-align:center;top:86px;font-size:25px">Automotive news and trends</h2>
  <p class="abs body-text" style="left:400px;width:400px;text-align:center;top:136px">Lorem ipsum dolor sit amet, consectetur adipisicing elit, sed do eiusmod tempor incididunt ut labore et dolore magna aliqua.</p>

  <div class="photo" style="left:264px;top:184px;width:118px;height:79px;background:linear-gradient(180deg,#c9cfd6,#6b7079 55%,#3a3c40)" role="img" aria-label="Dark saloon car on a road"><span class="badge">Automotive</span></div>
  <div class="news-title" style="left:406px;top:202px">2021 Vantor 9 Series gets fresh<br>styling and infotainment</div>
  <div class="photo" style="left:609px;top:184px;width:118px;height:79px;background:linear-gradient(135deg,#dfe3e7,#8a8f96 50%,#2f3135)" role="img" aria-label="Close-up of a tyre and wheel"><span class="badge">Automotive</span></div>
  <div class="news-title" style="left:750px;top:202px">The automobile club acquires<br>stakes in mobile security</div>

  <div class="photo" style="left:264px;top:285px;width:118px;height:79px;background:linear-gradient(135deg,#5a3a20,#c57a2a 50%,#2a1e14)" role="img" aria-label="Car interior with steering wheel"><span class="badge">Automotive</span></div>
  <div class="news-title" style="left:406px;top:303px">Kessa to use innovative AI to<br>boost efficiency</div>
  <div class="photo" style="left:609px;top:285px;width:118px;height:79px;background:linear-gradient(135deg,#f1d27a,#e0a92a 50%,#6a6a6a)" role="img" aria-label="Yellow sports car front view"><span class="badge">Automotive</span></div>
  <div class="news-title" style="left:750px;top:303px">Japan's automakers see<br>positive signs ahead</div>
</section>

<!-- FOOTER -->
<section style="top:3216px;height:257px;background:var(--footer)">
  <div class="photo" style="left:300px;top:0;width:900px;height:257px;background:radial-gradient(ellipse at 45% 90%,#3a2a22 0,#231c18 40%,var(--footer) 75%)" role="img" aria-label="Dimly lit car speedometer dial"></div>
  <div class="abs logo" style="left:264px;top:48px;font-size:13px"><i></i>Ridgeline Haulers</div>
  <h2 class="abs head" style="left:264px;top:92px;font-size:23px;color:#fff">Let's get connected</h2>
  <div class="btn" style="left:264px;top:137px;width:92px;height:35px;line-height:35px">Contact us</div>
  <div class="foot-col" style="left:566px"><b>MENU</b>About<br>Repair<br>Services<br>Contact</div>
  <div class="foot-col" style="left:667px"><b>LINKS</b>FAQ<br>Shop<br>Accessories<br>Community</div>
  <div class="foot-col" style="left:767px"><b>ADDRESS</b><br><div class="dots"><span></span><span></span><span></span></div>Powered by</div>
</section>

</body>
</html>
```